Business Card - Brisk Works
Stout Harbor BC
Project: Business Card - Brisk Works
Business Card - Brisk Works - Manufacturing
Creative Brief
Professional
Gordon Pratchett
gpratchett@stoutharbor-mail.com
"Build and Thrive"
emagineitgroup emagineitgroup
I accidentally erased #67, can it be put back on?
I like #105 as a start with the following changes: 1. the bottom portion of the card is black I would like this to be eliminated and center (2) shiny gold lines centered and measuring : TOP LINE - 2 6/8" AND THE BOTTOM LINE = 1 5/8" . These two lines should be centered . THE DISTANCE APART SHOULD BE 1/16". I would like for the two 'shiny gold lines' to be centered between the logo on top and my information below. I would also like for my name: GORDON PRATCHETT to be in bold black and all caps. I would like to see the rest of the info not in bold, but in black font. I would like the pareto chart (3) to the right on top of the black line to be completely eliminated. I only want to have a card that is one sided. I would also like to see the card as it is, currently, with the font in the black section on the lower half of the card, in white font.
Im liking the clear cards as well. Please give me more options on clear business cards that are perhaps not as generic.
glassfairy glassfairy
plz upload the logo file too
I have a current Business Card i would like to Add for an example. Please let me know where to add it.

```html
<!DOCTYPE html>
<html lang="en">
<head>
<meta charset="utf-8">
<title>Stout Harbor Business Card</title>
<link rel="stylesheet" href="https://fonts.googleapis.com/css2?family=Open+Sans:wght@400;600&display=swap">
<style>
  :root {
    --page: #d9d6d1;
    --frost-top: #f3f4f5;
    --frost-bottom: #dfe2e5;
    --panel: #2b2b2d;
    --gold: #c9a45a;
    --gold-light: #e8cf8f;
    --ink: #2a2a2a;
    --light-text: #f2f2f2;
    --muted-text: #d0d0d0;
  }
  * { margin: 0; padding: 0; box-sizing: border-box; }
  html, body { width: 1200px; height: 768px; overflow: hidden; background: var(--page); }
  .card {
    position: absolute; left: 100px; top: 98px;
    width: 1000px; height: 572px;
    box-shadow: 0 18px 40px rgba(0,0,0,0.18);
  }
  .card-shape { position: absolute; inset: 0; }
  .brand {
    position: absolute; left: 40px; top: 270px; width: 440px;
    display: flex; align-items: center; justify-content: center;
    font-family: "Open Sans", sans-serif; font-weight: 600;
    font-size: 30px; color: var(--ink); white-space: nowrap;
  }
  .brand-mark {
    width: 18px; height: 18px; margin-right: 14px; flex: none;
    background: var(--ink);
  }
  .details {
    position: absolute; left: 610px; top: 88px;
    font-family: "Open Sans", sans-serif; color: var(--light-text);
  }
  .person-name { font-size: 22px; font-weight: 600; line-height: 30px; }
  .person-role { font-size: 16px; line-height: 22px; color: var(--muted-text); margin-top: 2px; }
  .address { margin-top: 88px; font-size: 15px; line-height: 24px; color: var(--muted-text); }
  .contact-list { list-style: none; margin-top: 78px; font-size: 15px; color: var(--muted-text); }
  .contact-list li { display: flex; align-items: center; height: 25px; }
  .contact-icon { width: 14px; height: 14px; margin-right: 12px; flex: none; }
</style>
</head>
<body>
<div class="card">
  <svg class="card-shape" width="1000" height="572" viewBox="0 0 1000 572" aria-hidden="true">
    <defs>
      <linearGradient id="frost" x1="0" y1="0" x2="0.4" y2="1">
        <stop offset="0" stop-color="#f3f4f5"/>
        <stop offset="1" stop-color="#dfe2e5"/>
      </linearGradient>
      <linearGradient id="goldArc" x1="0" y1="0" x2="0" y2="1">
        <stop offset="0" stop-color="#e8cf8f"/>
        <stop offset="0.5" stop-color="#c9a45a"/>
        <stop offset="1" stop-color="#e8cf8f"/>
      </linearGradient>
    </defs>
    <rect width="1000" height="572" fill="url(#frost)"/>
    <path d="M480 0 Q640 286 480 572 L1000 572 L1000 0 Z" fill="#2b2b2d"/>
    <path d="M480 0 Q640 286 480 572" fill="none" stroke="url(#goldArc)" stroke-width="8"/>
  </svg>

  <div class="brand">
    <span class="brand-mark"></span>
    <span class="brand-name">Stout Harbor, Inc.</span>
  </div>

  <div class="details">
    <div class="person-name">Marla Quenby</div>
    <div class="person-role">consultant</div>
    <div class="address">27 5th floor Court<br>Harbor Lane RDG</div>
    <ul class="contact-list">
      <li><svg class="contact-icon" viewBox="0 0 14 14"><path d="M3 1 L5 1 L6 4 L4.5 5 Q5.5 8 9 9.5 L10 8 L13 9 L13 11 Q12 13 10 13 Q2 11 1 3 Q1 1 3 1Z" fill="currentColor"/></svg>014 552 8170</li>
      <li><svg class="contact-icon" viewBox="0 0 14 14"><rect x="3.5" y="0.5" width="7" height="13" rx="1.5" fill="currentColor"/><rect x="5" y="2.5" width="4" height="7.5" fill="#2b2b2d"/></svg>014 552 8170</li>
      <li><svg class="contact-icon" viewBox="0 0 14 14"><rect x="1" y="5" width="12" height="7" rx="1" fill="currentColor"/><rect x="3.5" y="1" width="7" height="4" fill="currentColor"/></svg>014 552 8170</li>
      <li><svg class="contact-icon" viewBox="0 0 14 14"><rect x="1" y="3" width="12" height="8" fill="currentColor"/><path d="M1 3 L7 8 L13 3" fill="none" stroke="#2b2b2d" stroke-width="1.2"/></svg>mquenby@email.net</li>
      <li><svg class="contact-icon" viewBox="0 0 14 14"><circle cx="7" cy="7" r="6" fill="currentColor"/><path d="M1 7 H13 M7 1 Q3 7 7 13 M7 1 Q11 7 7 13" fill="none" stroke="#2b2b2d" stroke-width="1"/></svg>www.stoutharbor-site.com</li>
    </ul>
  </div>
</div>
</body>
</html>
```